web page layout, style , color, font & flow design

We are developing a single page application. The SPA (single page application) will display natural gas pipeline flow data once the customer logs on. The customer has a choice of the region, the pipeline, the zone on the pipeline, whether the point is a delivery point or receipt point and the state the pipeline flows through.
we have jumpstarted the project and are attaching a pdf of the same.

we are using mockingbird for the wireframe. any designer is free to use this tool to make changes.

A mockingbird wireframe link is added below. you are free to use it and to make changes. please save the changed wireframe in a different name

we are looking for inputs on layout, style , color, font & flow.

A logo jpg file has also been attached.

Target Market(s)

this single web page is going to be used by natural gas traders and schedulers day in and day out. the application is more of business to business corporate application.

Industry/Entity Type

Delivery

Requirements
Must have
• layout ,flow, size, color, font , ease of use.

```html
<!DOCTYPE html>
<html lang="en">
<head>
<meta charset="utf-8">
<title>Wholesale NG Supply Analysis</title>
<link rel="stylesheet" href="https://fonts.googleapis.com/css2?family=Arimo:wght@400;700&family=Tinos&display=swap">
<style>
:root{
  --page-top:#ebebeb;
  --page-bottom:#4b6650;
  --panel:#ffffff;
  --tab-bar:#dedede;
  --tab-idle:#a9a9a9;
  --ink:#111111;
  --brand:#2f6e9e;
  --field-hint:#b8b8b8;
  --field-edge:#b0b0b0;
  --arrow:#a08e00;
  --submit-bg:#d9d9d9;
  --list-ink:#1a6a30;
  --list-active:#e07a10;
  --head-bg:#fcc8fc;
  --head-ink:#2aa4dc;
  --row-cyan:#c8fcfc;
  --row-pink:#fcc8fc;
  --grid:#c4c4c4;
}
*{box-sizing:border-box;margin:0;padding:0}
html,body{width:1200px;height:801px;overflow:hidden}
body{position:relative;font-family:"Arimo",Arial,sans-serif;
  background:linear-gradient(var(--page-top) 0 361px,var(--page-bottom) 361px 100%)}
.brand{position:absolute;left:36px;top:23px;width:89px;height:75px;border:1px solid #d0d0d0;
  background:#e4e6ea;display:flex;align-items:center;justify-content:center;gap:5px;
  font-size:14px;font-weight:700;color:var(--brand)}
.brand-dot{width:9px;height:9px;border-radius:50%;background:var(--brand)}
.page-title{position:absolute;left:0;width:1200px;top:36px;text-align:center;
  font-family:"Tinos","Times New Roman",serif;font-weight:400;font-size:35px;color:var(--ink)}
.panel{position:absolute;left:36px;top:120px;width:1133px;height:621px;background:var(--panel);
  border-radius:7px;overflow:hidden}
.tabs{display:flex;height:61px;background:var(--tab-bar);list-style:none}
.tab{width:181px;display:flex;align-items:center;justify-content:center;font-size:19px;color:var(--tab-idle)}
.tab.is-active{background:var(--panel);color:var(--ink);box-shadow:3px 0 3px -1px rgba(0,0,0,.25)}
.filters{position:absolute;left:37px;top:110px;width:1062px;height:90px}
.select{position:absolute;width:300px;height:35px;background:#fff;border:2px solid var(--field-edge);
  box-shadow:inset 2px 2px 4px rgba(0,0,0,.25);font-size:15px;color:var(--field-hint);
  padding:9px 0 0 12px}
.select::after{content:"";position:absolute;right:0;top:0;width:36px;height:31px;background:#fff;
  border-left:1px solid #ddd}
.select svg{position:absolute;right:10px;top:12px;z-index:1}
.submit{position:absolute;left:984px;top:52px;width:76px;height:36px;background:var(--submit-bg);
  border:none;font-family:inherit;font-size:15px;color:var(--arrow);box-shadow:0 1px 2px rgba(0,0,0,.2)}
.pipelines{position:absolute;left:40px;top:243px;list-style:none;font-size:13px;line-height:19.3px;color:var(--list-ink)}
.pipelines .is-active{color:var(--list-active)}
.flow-table{position:absolute;left:289px;top:243px;border-collapse:collapse;border:1px solid var(--grid)}
.flow-table th{height:48px;background:var(--head-bg);color:var(--head-ink);font-weight:400;font-size:15.5px;
  text-align:left;padding:0 0 0 17px;border:1px solid var(--grid)}
.flow-table td{height:30px;border:1px solid var(--grid)}
.flow-table tbody tr:nth-child(odd) td{background:var(--row-cyan)}
.flow-table tbody tr:nth-child(even) td{background:var(--row-pink)}
</style>
</head>
<body>
<div class="brand"><span class="brand-dot"></span>Flowmark</div>
<h1 class="page-title">Wholesale NG Supply Analysis</h1>

<main class="panel">
  <ul class="tabs">
    <li class="tab is-active">North East</li>
    <li class="tab">Mid West</li>
    <li class="tab">South East</li>
    <li class="tab">South West</li>
    <li class="tab">Central</li>
    <li class="tab">West</li>
  </ul>

  <form class="filters">
    <div class="select" style="left:0;top:0">Location Type<svg width="18" height="10"><path d="M0 0H18L9 9Z" fill="#a08e00"/></svg></div>
    <div class="select" style="left:325px;top:0">States<svg width="18" height="10"><path d="M0 0H18L9 9Z" fill="#a08e00"/></svg></div>
    <div class="select" style="left:649px;top:0">Zones<svg width="18" height="10"><path d="M0 0H18L9 9Z" fill="#a08e00"/></svg></div>
    <div class="select" style="left:0;top:52px">gas day<svg width="18" height="10"><path d="M0 0H18L9 9Z" fill="#a08e00"/></svg></div>
    <div class="select" style="left:325px;top:52px">Cycle<svg width="18" height="10"><path d="M0 0H18L9 9Z" fill="#a08e00"/></svg></div>
    <div class="select" style="left:649px;top:52px">Posting Time<svg width="18" height="10"><path d="M0 0H18L9 9Z" fill="#a08e00"/></svg></div>
    <button type="button" class="submit">SUBMIT</button>
  </form>

  <ul class="pipelines">
    <li>Alder Ridge</li>
    <li>CPL</li>
    <li>Dunmore</li>
    <li>Eastern Bay NG</li>
    <li class="is-active">East Valley NG</li>
    <li>Elmstead Gas</li>
    <li>Everline Inc.</li>
    <li>Granite Ledge Gas</li>
    <li>Ironwood</li>
    <li>Harbor &amp; North East</li>
    <li>Milestone Pipeline</li>
    <li>Northern Fuel Gas Supply Corp.</li>
    <li>Pinecrest NG</li>
    <li>St. Clair Gas</li>
    <li>Tamarack Gas</li>
    <li>Tidemark</li>
    <li>Transvale</li>
  </ul>

  <table class="flow-table" aria-label="Pipeline flow data, awaiting a query">
    <colgroup>
      <col style="width:112px"><col style="width:103px"><col style="width:109px"><col style="width:103px">
      <col style="width:138px"><col style="width:103px"><col style="width:140px">
    </colgroup>
    <thead>
      <tr><th>Gas Day</th><th>Location</th><th>Loc_Name</th><th>Flow_Ind</th><th>Loc_Desc</th><th>Op_Cap</th><th>Sch_Cap</th></tr>
    </thead>
    <tbody>
      <tr><td></td><td></td><td></td><td></td><td></td><td></td><td></td></tr>
      <tr><td></td><td></td><td></td><td></td><td></td><td></td><td></td></tr>
      <tr><td></td><td></td><td></td><td></td><td></td><td></td><td></td></tr>
      <tr><td></td><td></td><td></td><td></td><td></td><td></td><td></td></tr>
      <tr><td></td><td></td><td></td><td></td><td></td><td></td><td></td></tr>
      <tr><td></td><td></td><td></td><td></td><td></td><td></td><td></td></tr>
      <tr><td></td><td></td><td></td><td></td><td></td><td></td><td></td></tr>
      <tr><td></td><td></td><td></td><td></td><td></td><td></td><td></td></tr>
      <tr><td></td><td></td><td></td><td></td><td></td><td></td><td></td></tr>
    </tbody>
  </table>
</main>
</body>
</html>
```